Brownie Snack Packaging

Design the film wrapper packaging for a brownie snack. It needs to be cohesive with our existing product line (please review attached photos), but still differentiated from it to avoid customer confusion.
Brief is outlined in the images attached. Please review prior to submitting designs. All designs should have the iridescent white pearl packaging color, with the text:
High Protein Brownie
10g Protein
Vegan
Gluten-Free
No Added Sugars
We would like to see designs with square packaging with a mouth-watering brownie image being the most prominent. Logo of brand "ORUNE" should be in upper right corner.
Note: we have another product line of cashew butter sachets that are pink, blue, & chocolate - I'm attaching those for reference so you can design these brownies to look somewhat related to the cashew butters.
Look and feel
Each slider illustrates characteristics of the customer's brand and the style your logo design should communicate.

```html
<!DOCTYPE html>
<html lang="en">
<head>
<meta charset="utf-8">
<title>ORUNE High Protein Brownie – Wrapper Front</title>
<link rel="stylesheet" href="https://fonts.googleapis.com/css2?family=Gloock&family=Questrial&display=swap">
<style>
  :root {
    --page-bg: #ececec;
    --pack-white: #ffffff;
    --pack-edge: #d6d6d6;
    --gold: #b88a2c;
    --ink: #1d1a19;
    --callout-ink: #3a3430;
    --cream: #f3e8d6;
    --cocoa: #4a3029;
    --claim-text: #f3e8d6;
    --brownie-dark: #3d2118;
    --brownie-mid: #6b3a27;
    --brownie-light: #8a5034;
  }
  * { margin: 0; padding: 0; box-sizing: border-box; }
  html, body {
    width: 1200px;
    height: 900px;
    overflow: hidden;
    background: var(--page-bg);
  }
  .wrapper-front {
    position: absolute;
    left: 210px;
    top: 60px;
    width: 780px;
    height: 780px;
    background: var(--pack-white);
    border: 1px solid var(--pack-edge);
    font-family: "Questrial", "Helvetica Neue", Arial, sans-serif;
    color: var(--ink);
  }
  .protein-callout {
    position: absolute;
    left: 65px;
    top: 85px;
    height: 98px;
    padding-left: 18px;
    border-left: 3px solid var(--gold);
    display: flex;
    align-items: center;
    font-size: 24px;
    line-height: 27px;
    color: var(--callout-ink);
  }
  .brand-name {
    position: absolute;
    left: 606px;
    top: 82px;
    width: 106px;
    height: 294px;
    writing-mode: vertical-rl;
    transform: rotate(180deg);
    text-align: center;
    font-family: "Questrial", "Helvetica Neue", Arial, sans-serif;
    font-size: 84px;
    line-height: 106px;
    color: var(--gold);
  }
  .brownie-photo {
    position: absolute;
    left: 134px;
    top: 100px;
    width: 470px;
    height: 345px;
    z-index: 2;
    border-radius: 10px;
    clip-path: polygon(92px 0, 100% 0, 100% 100%, 0 100%, 0 96px, 92px 96px);
    background:
      radial-gradient(ellipse at 50% 25%, var(--brownie-dark) 0%, transparent 55%),
      linear-gradient(180deg, var(--brownie-mid) 0%, var(--brownie-light) 45%, var(--brownie-mid) 100%);
  }
  .name-band {
    position: absolute;
    left: 34px;
    top: 402px;
    width: 710px;
    height: 194px;
    z-index: 1;
    background: var(--cream);
    border-radius: 12px;
    padding-top: 62px;
    text-align: center;
    font-family: "Gloock", Georgia, serif;
    font-weight: 400;
    color: var(--ink);
  }
  .name-band .name-line-small {
    display: block;
    font-size: 37px;
    line-height: 42px;
    letter-spacing: 3px;
  }
  .name-band .name-line-large {
    display: block;
    font-size: 62px;
    line-height: 66px;
    letter-spacing: 3px;
  }
  .claims-bar {
    position: absolute;
    left: 34px;
    top: 610px;
    width: 710px;
    height: 92px;
    background: var(--cocoa);
    border-radius: 10px;
    display: flex;
    align-items: center;
    list-style: none;
  }
  .claims-bar .claim {
    flex: 1;
    padding: 12px 0;
    text-align: center;
    font-size: 23px;
    line-height: 26px;
    letter-spacing: 0.5px;
    color: var(--claim-text);
  }
  .claims-bar .claim + .claim {
    border-left: 2px solid var(--claim-text);
  }
</style>
</head>
<body>
  <main class="wrapper-front">
    <div class="protein-callout">10g<br>protein</div>
    <div class="brand-name">ORUNE</div>
    <div class="brownie-photo" role="img" aria-label="Stack of three chocolate brownie squares with melted chocolate drizzled over them"></div>
    <h1 class="name-band">
      <span class="name-line-small">HIGH PROTEIN</span>
      <span class="name-line-large">BROWNIE</span>
    </h1>
    <ul class="claims-bar">
      <li class="claim">no added<br>sugars</li>
      <li class="claim">vegan</li>
      <li class="claim">gluten<br>free</li>
    </ul>
  </main>
</body>
</html>
```